Water Remediation & Restoration Industry

Our company is in need of a trifold design for the water remediation & restoration industry. This brochure's main purpose is to help our company advertise its services to our community as well as insurance company's, home owners, and building managers. We currently run a commercial cleaning company and this is a new branch of service that we offer. We would like for the colors to coordinate with the logo which are royal blue, grey and white. We would like for the brochure to incorporate photos showing thermal imaging, equipment such as fans, dehumidifiers etc, water floods/leaks. We are a QWSBT Certified firm and the details to include are the following:
Phone Number: 1-866-555-0183
Website: www.tplvworks.org
24 Hour Emergency Services
Emergency Mitigation
Water Extraction
Structural Drying
Dehumidication
Mold Remediation
Water Damage Restoration
Fire & Smoke Cleanup
Sewage & Toilet Overflows
Carpet & Upholstery Cleaning
Contents Cleaning
Monitoring/Coordination
Antimicrobial Application
Smoke & Odor Removal

```html
<!DOCTYPE html>
<html lang="en">
<head>
<meta charset="utf-8">
<title>Tri-Point Lakeview Works — Trifold Brochure</title>
<link href="https://fonts.googleapis.com/css2?family=Montserrat:wght@500;700;800&family=Open+Sans:wght@400;600&display=swap" rel="stylesheet">
<style>
  :root {
    --royal: #2b2f92;
    --navy: #1c1e66;
    --grey: #b9bbc0;
    --grey-dark: #8d9096;
    --white: #ffffff;
    --paper: #f4f5f8;
    --ink: #22243a;
    --stage: #5b5f66;
  }
  * { box-sizing: border-box; margin: 0; padding: 0; }
  html, body { width: 1200px; height: 1200px; overflow: hidden; }
  body {
    background: radial-gradient(circle at 50% 40%, #6b6f76, var(--stage));
    font-family: "Open Sans", Arial, sans-serif;
    color: var(--ink);
    position: relative;
  }
  .sheet {
    position: absolute;
    left: 60px;
    width: 1080px;
    height: 540px;
    background: var(--white);
    box-shadow: 0 10px 30px rgba(0,0,0,.35);
    overflow: hidden;
  }
  .sheet--outside { top: 30px; }
  .sheet--inside { top: 630px; }
  .sheet__art { position: absolute; inset: 0; width: 1080px; height: 540px; }
  .fold {
    position: absolute; top: 0; bottom: 0; width: 1px;
    background: rgba(0,0,0,.08);
  }
  .fold--a { left: 360px; }
  .fold--b { left: 720px; }
  .block { position: absolute; }

  /* outside: efficiency panel */
  .efficiency { left: 28px; top: 168px; width: 300px; color: var(--white); }
  .efficiency__title {
    font-family: "Montserrat", Arial, sans-serif;
    font-weight: 800; font-size: 17px; line-height: 1.15;
    letter-spacing: .5px; margin-bottom: 10px;
  }
  .efficiency p { font-size: 9.5px; line-height: 1.45; margin-bottom: 8px; }

  /* outside: contact panel */
  .contact { left: 380px; top: 36px; width: 320px; text-align: center; font-size: 10px; line-height: 1.4; }
  .contact__item { margin-bottom: 12px; }
  .contact__icon { display: block; margin: 0 auto 3px; }

  .brand {
    display: flex; align-items: center; gap: 10px;
    font-family: "Montserrat", Arial, sans-serif;
  }
  .brand__mark { width: 16px; height: 16px; border-radius: 50%; flex: none; }
  .brand__name { font-weight: 800; font-size: 34px; letter-spacing: 2px; }
  .brand__tag { font-family: "Montserrat", Arial, sans-serif; font-weight: 700; font-size: 11px; }

  .back-brand { left: 392px; top: 452px; color: var(--white); }
  .back-brand .brand__mark { background: var(--white); }
  .back-brand .brand__tag { margin-top: 2px; }
  .badge {
    position: absolute; left: 650px; top: 462px;
    width: 44px; height: 50px; border-radius: 4px;
    background: var(--white); border: 2px solid var(--grey);
  }

  /* outside: cover panel */
  .cover-brand { left: 780px; top: 48px; color: var(--royal); }
  .cover-brand .brand__mark { background: var(--royal); }
  .cover-brand .brand__name { font-size: 40px; }
  .cover-brand .brand__tag { color: var(--royal); margin-top: 4px; }
  .cover-title {
    left: 744px; top: 410px; width: 320px; color: var(--white);
    font-family: "Montserrat", Arial, sans-serif; font-weight: 800;
    font-size: 24px; line-height: 1.15; letter-spacing: 1px;
  }
  .cover-url {
    left: 744px; top: 488px; color: var(--white);
    font-family: "Montserrat", Arial, sans-serif; font-size: 12px; letter-spacing: 4px;
  }

  /* inside */
  .pill {
    display: block; width: 280px; margin: 0 auto 16px;
    background: var(--royal); color: var(--white);
    border-radius: 18px; border-bottom: 3px solid var(--grey);
    font-family: "Montserrat", Arial, sans-serif; font-weight: 700;
    font-size: 14px; letter-spacing: .5px; text-align: center; padding: 7px 0;
  }
  .copy p { font-size: 10px; line-height: 1.45; margin-bottom: 10px; }
  .vision { left: 30px; top: 36px; width: 300px; }
  .mission { left: 390px; top: 36px; width: 300px; }
  .services { left: 750px; top: 36px; width: 300px; }
  .services__list { list-style: none; margin-left: 30px; }
  .services__list li {
    display: flex; align-items: center; gap: 8px;
    font-size: 10px; line-height: 1; margin-bottom: 6.6px;
  }
  .services__list svg { flex: none; }
  .inside-url {
    left: 820px; top: 495px; color: var(--white);
    font-family: "Montserrat", Arial, sans-serif; font-size: 12px; letter-spacing: 4px;
  }
</style>
</head>
<body>

<!-- Outside of the trifold -->
<section class="sheet sheet--outside" aria-label="Brochure outside">
  <svg class="sheet__art" viewBox="0 0 1080 540">
    <defs>
      <linearGradient id="photoCool" x1="0" y1="0" x2="1" y2="1">
        <stop offset="0" stop-color="#dfe3ea"/><stop offset="1" stop-color="#8f9ab8"/>
      </linearGradient>
      <linearGradient id="photoRoom" x1="0" y1="0" x2="0" y2="1">
        <stop offset="0" stop-color="#e9ebef"/><stop offset="1" stop-color="#b9a58c"/>
      </linearGradient>
      <linearGradient id="blueFade" x1="0" y1="0" x2="1" y2="1">
        <stop offset="0" stop-color="#2b2f92"/><stop offset="1" stop-color="#1c1e66"/>
      </linearGradient>
    </defs>

    <!-- efficiency panel -->
    <rect x="0" y="0" width="360" height="540" fill="url(#blueFade)"/>
    <path role="img" aria-label="Photo of cleaning staff mopping and tidying an office" d="M0 0 H360 V110 Q200 175 0 150 Z" fill="url(#photoCool)"/>
    <path d="M0 150 Q200 175 360 110 V122 Q200 190 0 162 Z" fill="var(--grey)"/>
    <path role="img" aria-label="Photo of a worker mopping a floor beside a cleaning cart" d="M0 420 Q180 400 360 440 V540 H0 Z" fill="url(#photoCool)"/>
    <path d="M0 412 Q180 390 360 430 V442 Q180 402 0 424 Z" fill="var(--grey)"/>

    <!-- contact panel -->
    <path d="M360 400 Q520 350 720 420 V540 H360 Z" fill="url(#blueFade)"/>
    <path d="M360 388 Q520 338 720 408 V420 Q520 352 360 400 Z" fill="var(--grey)"/>
    <circle cx="560" cy="308" r="70" fill="var(--royal)"/>
    <circle role="img" aria-label="Photo of a floor buffer polishing a hallway" cx="560" cy="308" r="64" fill="url(#photoRoom)"/>

    <!-- cover panel -->
    <path role="img" aria-label="Photo of a smiling janitor with a mop in an office next to a wet floor sign" d="M720 150 H1080 V350 Q900 400 720 320 Z" fill="url(#photoRoom)"/>
    <path d="M720 320 Q900 400 1080 350 V366 Q900 416 720 336 Z" fill="var(--grey)"/>
    <path d="M720 336 Q900 416 1080 366 V540 H720 Z" fill="url(#blueFade)"/>
  </svg>
  <div class="fold fold--a"></div>
  <div class="fold fold--b"></div>

  <div class="block efficiency">
    <h2 class="efficiency__title">EXPERIENCE<br>HIGH-TECH EFFICIENCY</h2>
    <p>Tri-Point Lakeview Works follows a technology-based service delivery process. In our company, employees communicate with each other using smartphone/tablet apps so that they can track every cleaning team's whereabouts.</p>
    <p>This enables main office managers to efficiently monitor work progress in real time. With this high-tech infrastructure in place, our cleaners can be able to relay on-the-spot customer requests to us immediately. We can then issue instructions just as quickly to employees on site.</p>
  </div>

  <div class="block contact">
    <div class="contact__item">
      <svg class="contact__icon" width="10" height="13" viewBox="0 0 10 13"><path d="M5 0a5 5 0 0 0-5 5c0 3.5 5 8 5 8s5-4.5 5-8a5 5 0 0 0-5-5zm0 7a2 2 0 1 1 0-4 2 2 0 0 1 0 4z" fill="var(--royal)"/></svg>
      Tri-Point Lakeview Works<br>14 Harlow Avenue<br>Brenton Falls, Kentucky 40999
    </div>
    <div class="contact__item">
      <svg class="contact__icon" width="11" height="11" viewBox="0 0 24 24"><path d="M6.6 10.8a15.1 15.1 0 0 0 6.6 6.6l2.2-2.2c.3-.3.7-.4 1-.2 1.1.4 2.3.6 3.6.6.6 0 1 .4 1 1V20c0 .6-.4 1-1 1A17 17 0 0 1 3 4c0-.6.4-1 1-1h3.5c.6 0 1 .4 1 1 0 1.3.2 2.5.6 3.6.1.3 0 .7-.2 1z" fill="var(--royal)"/></svg>
      1-866-555-0183
    </div>
    <div class="contact__item">
      <svg class="contact__icon" width="12" height="9" viewBox="0 0 12 9"><rect width="12" height="9" rx="1" fill="var(--royal)"/><path d="M0 1l6 4 6-4" stroke="#fff" fill="none"/></svg>
      office@tplvworks.org
    </div>
    <div class="contact__item">
      <svg class="contact__icon" width="11" height="11" viewBox="0 0 12 12"><circle cx="6" cy="6" r="5.5" fill="var(--royal)"/><path d="M1 6h10M6 1c2 2 2 8 0 10M6 1c-2 2-2 8 0 10" stroke="#fff" stroke-width=".8" fill="none"/></svg>
      www.tplvworks.org
    </div>
  </div>

  <div class="block brand back-brand">
    <span class="brand__mark"></span>
    <div>
      <div class="brand__name">TPLV</div>
      <div class="brand__tag">Commercial Cleaning &amp; Restoration</div>
    </div>
  </div>
  <div class="badge" aria-label="Certified firm badge"></div>

  <div class="block brand cover-brand">
    <span class="brand__mark"></span>
    <div>
      <div class="brand__name">TPLV</div>
      <div class="brand__tag">Commercial Cleaning &amp; Restoration</div>
    </div>
  </div>
  <h1 class="block cover-title">DEDICATION THROUGH COMMUNICATION</h1>
  <div class="block cover-url">www.tplvworks.org</div>
</section>

<!-- Inside of the trifold -->
<section class="sheet sheet--inside" aria-label="Brochure inside">
  <svg class="sheet__art" viewBox="0 0 1080 540">
    <defs>
      <linearGradient id="photoWarm" x1="0" y1="0" x2="1" y2="1">
        <stop offset="0" stop-color="#d9c79a"/><stop offset=".6" stop-color="#3a3a66"/><stop offset="1" stop-color="#e4d25a"/>
      </linearGradient>
      <linearGradient id="photoCarpet" x1="0" y1="0" x2="1" y2="1">
        <stop offset="0" stop-color="#e6e4e2"/><stop offset="1" stop-color="#a9aab0"/>
      </linearGradient>
      <linearGradient id="blueBand" x1="0" y1="0" x2="1" y2="0">
        <stop offset="0" stop-color="#1c1e66"/><stop offset="1" stop-color="#2b2f92"/>
      </linearGradient>
    </defs>
    <rect width="1080" height="540" fill="var(--paper)"/>
    <rect x="360" width="360" height="540" fill="var(--white)"/>
    <path d="M280 540 Q650 450 1080 400 V540 Z" fill="url(#blueBand)"/>
    <path d="M270 528 Q650 434 1080 384 V400 Q650 450 280 540 Z" fill="var(--grey)"/>
    <path role="img" aria-label="Photo of a smiling housekeeper in uniform with a cleaning cart" d="M0 330 Q200 380 560 480 Q420 520 380 540 H0 Z" fill="url(#photoWarm)"/>
    <circle cx="560" cy="455" r="68" fill="var(--royal)"/>
    <circle role="img" aria-label="Photo of a carpet extraction wand cleaning a carpet" cx="560" cy="455" r="62" fill="url(#photoCarpet)"/>
  </svg>
  <div class="fold fold--a"></div>
  <div class="fold fold--b"></div>

  <div class="block copy vision">
    <h2 class="pill">OUR VISION</h2>
    <p>Tri-Point Lakeview Works will be one of the top independently owned commercial cleaning services, serving the central and eastern part of Kentucky.</p>
    <p>Our vision is to become the leader in commercial cleaning and building services industry by using modern technology to blaze the trail that others will follow when it comes to providing quality services and exceptional customer service.</p>
    <p>We will be relentless in our commitment to fulfill our vision and offer our clients personalized service.</p>
  </div>

  <div class="block copy mission">
    <h2 class="pill">OUR MISSION</h2>
    <p>Tri-Point Lakeview Works is committed to providing an unsurpassed level of janitorial services and building long-lasting relationships with clients. We accomplish this by using modern technology to communicate effectively with client's and employees.</p>
    <p>Our team leaders assist clients in defining their needs and communicate those needs to our employees. We act with integrity in all aspects of our business at all times. Our goal is to deliver a consistently high level of janitorial services that are within your budget.</p>
    <p>We hold each and every client in the highest regard and promise to provide exceptional service. This is accomplished by experienced, professional employees who follow our company's meticulous cleaning standards. We provide quality cleaning services, exceptional customer service, scheduled site inspections, and customer surveys while keeping communication lines open for our customers so that their every need is fulfilled.</p>
  </div>

  <div class="block copy services">
    <h2 class="pill">SERVICES WE OFFER</h2>
    <p>Our company specializes in cleaning medical facilities and class-A office spaces. You can contact us to request:</p>
    <ul class="services__list">
      <li><svg width="11" height="11" viewBox="0 0 12 12"><circle cx="6" cy="6" r="6" fill="var(--royal)"/><path d="M3.3 6.2l1.8 1.8 3.6-3.6" stroke="#fff" stroke-width="1.5" fill="none"/></svg>24 Hour Emergency Services</li>
      <li><svg width="11" height="11" viewBox="0 0 12 12"><circle cx="6" cy="6" r="6" fill="var(--royal)"/><path d="M3.3 6.2l1.8 1.8 3.6-3.6" stroke="#fff" stroke-width="1.5" fill="none"/></svg>Emergency Mitigation</li>
      <li><svg width="11" height="11" viewBox="0 0 12 12"><circle cx="6" cy="6" r="6" fill="var(--royal)"/><path d="M3.3 6.2l1.8 1.8 3.6-3.6" stroke="#fff" stroke-width="1.5" fill="none"/></svg>Water Extraction</li>
      <li><svg width="11" height="11" viewBox="0 0 12 12"><circle cx="6" cy="6" r="6" fill="var(--royal)"/><path d="M3.3 6.2l1.8 1.8 3.6-3.6" stroke="#fff" stroke-width="1.5" fill="none"/></svg>Structural Drying</li>
      <li><svg width="11" height="11" viewBox="0 0 12 12"><circle cx="6" cy="6" r="6" fill="var(--royal)"/><path d="M3.3 6.2l1.8 1.8 3.6-3.6" stroke="#fff" stroke-width="1.5" fill="none"/></svg>Dehumidication</li>
      <li><svg width="11" height="11" viewBox="0 0 12 12"><circle cx="6" cy="6" r="6" fill="var(--royal)"/><path d="M3.3 6.2l1.8 1.8 3.6-3.6" stroke="#fff" stroke-width="1.5" fill="none"/></svg>Mold Remediation</li>
      <li><svg width="11" height="11" viewBox="0 0 12 12"><circle cx="6" cy="6" r="6" fill="var(--royal)"/><path d="M3.3 6.2l1.8 1.8 3.6-3.6" stroke="#fff" stroke-width="1.5" fill="none"/></svg>Water Damage Restoration</li>
      <li><svg width="11" height="11" viewBox="0 0 12 12"><circle cx="6" cy="6" r="6" fill="var(--royal)"/><path d="M3.3 6.2l1.8 1.8 3.6-3.6" stroke="#fff" stroke-width="1.5" fill="none"/></svg>Fire &amp; Smoke Cleanup</li>
      <li><svg width="11" height="11" viewBox="0 0 12 12"><circle cx="6" cy="6" r="6" fill="var(--royal)"/><path d="M3.3 6.2l1.8 1.8 3.6-3.6" stroke="#fff" stroke-width="1.5" fill="none"/></svg>Sewage &amp; Toilet Overflows</li>
      <li><svg width="11" height="11" viewBox="0 0 12 12"><circle cx="6" cy="6" r="6" fill="var(--royal)"/><path d="M3.3 6.2l1.8 1.8 3.6-3.6" stroke="#fff" stroke-width="1.5" fill="none"/></svg>Carpet &amp; Upholstery Cleaning</li>
      <li><svg width="11" height="11" viewBox="0 0 12 12"><circle cx="6" cy="6" r="6" fill="var(--royal)"/><path d="M3.3 6.2l1.8 1.8 3.6-3.6" stroke="#fff" stroke-width="1.5" fill="none"/></svg>Contents Cleaning</li>
      <li><svg width="11" height="11" viewBox="0 0 12 12"><circle cx="6" cy="6" r="6" fill="var(--royal)"/><path d="M3.3 6.2l1.8 1.8 3.6-3.6" stroke="#fff" stroke-width="1.5" fill="none"/></svg>Monitoring/Coordination</li>
      <li><svg width="11" height="11" viewBox="0 0 12 12"><circle cx="6" cy="6" r="6" fill="var(--royal)"/><path d="M3.3 6.2l1.8 1.8 3.6-3.6" stroke="#fff" stroke-width="1.5" fill="none"/></svg>Antimicrobial Application</li>
      <li><svg width="11" height="11" viewBox="0 0 12 12"><circle cx="6" cy="6" r="6" fill="var(--royal)"/><path d="M3.3 6.2l1.8 1.8 3.6-3.6" stroke="#fff" stroke-width="1.5" fill="none"/></svg>Smoke &amp; Odor Removal</li>
    </ul>
  </div>

  <div class="block inside-url">www.tplvworks.org</div>
</section>

</body>
</html>
```